Business Card & Letterhead Design

We a financial advice company based in Australia. We provide advice to wealthy farmers.

We are changing our business name FROM Brightmere Financial TO Calderstone Wealth and we need a new letterhead and double sided business card design

Attached is designs from our previous branding (Brightmere Financial) as it includes all the details we require on the new Calderstone Wealth business cards and letterhead.

```html
<!DOCTYPE html>
<html lang="en">
<head>
<meta charset="utf-8">
<title>Calderstone Wealth Letterhead</title>
<link rel="stylesheet" href="https://fonts.googleapis.com/css2?family=Roboto:wght@400&display=swap">
<style>
  :root {
    --backdrop: #d4d4d4;
    --paper: #f8f8f8;
    --ink: #333333;
    --ink-soft: #4a4a4a;
    --faint-mark: #ebebeb;
  }
  * { box-sizing: border-box; margin: 0; padding: 0; }
  html, body {
    width: 1152px; height: 1200px; overflow: hidden;
    background: var(--backdrop);
    font-family: "Roboto", Arial, sans-serif;
    color: var(--ink);
  }
  .letterhead {
    position: absolute; left: 158px; top: 20px;
    width: 835px; height: 1160px;
    background: var(--paper);
  }
  .brand {
    position: absolute; left: 51px; top: 45px; width: 316px;
    text-align: center;
  }
  .brand-circle { display: block; margin: 0 auto 10px; }
  .brand-name {
    font-size: 27px; font-weight: 400; letter-spacing: 1px;
    text-transform: uppercase; color: var(--ink); line-height: 1;
    white-space: nowrap;
  }
  .brand-tagline {
    margin-top: 3px; font-size: 10px; letter-spacing: 4.2px;
    text-transform: uppercase; color: var(--ink-soft);
    white-space: nowrap;
  }
  .contact {
    position: absolute; right: 51px; top: 42px;
    text-align: right; font-size: 13.2px; line-height: 16.5px;
  }
  .contact-address { margin-bottom: 6px; }
  .contact-line { display: flex; justify-content: flex-end; align-items: center; gap: 7px; }
  .contact-line svg { width: 10px; height: 10px; flex: none; }
  .watermark {
    position: absolute; left: 230px; top: 394px;
  }
  .footer {
    position: absolute; left: 51px; right: 51px; bottom: 42px;
    font-size: 13.2px; line-height: 16.5px;
  }
  .footer-licensee { position: absolute; left: 0; bottom: 0; }
  .footer-rep { position: absolute; left: 311px; bottom: 0; }
  .footer-trust { position: absolute; right: 0; bottom: 0; }
  .footer-divider {
    position: absolute; bottom: 0; width: 2.5px; background: var(--ink);
  }
  .footer-divider.first { left: 276px; height: 59px; }
  .footer-divider.second { left: 519px; height: 43px; }
</style>
</head>
<body>
  <main class="letterhead">
    <header>
      <div class="brand">
        <svg class="brand-circle" width="86" height="86" viewBox="0 0 86 86" aria-hidden="true">
          <circle cx="43" cy="43" r="41" fill="none" stroke="var(--ink)" stroke-width="2.5"/>
        </svg>
        <div class="brand-name">Calderstone Wealth</div>
        <div class="brand-tagline">Strategic Financial Advice</div>
      </div>

      <address class="contact" style="font-style:normal">
        <div class="contact-address">
          Suite 7C, 48 Tallow St<br>
          Riverbend QLD 4170<br>
          PO Box 5128<br>
          Westvale QLD 4170
        </div>
        <div class="contact-line">(07) 3555 0142
          <svg viewBox="0 0 10 10" aria-label="Phone"><path d="M2 1 L3.6 1 L4.3 3 L3.2 3.8 Q4 5.8 6.2 6.8 L7 5.7 L9 6.4 L9 8 Q8.6 9 7.5 9 Q1 8.4 1 2.5 Q1 1.2 2 1Z" fill="var(--ink)"/></svg>
        </div>
        <div class="contact-line">(07) 3555 0187
          <svg viewBox="0 0 10 10" aria-label="Fax"><rect x="2.5" y="1" width="5" height="2.5" fill="var(--ink)"/><rect x="1" y="4" width="8" height="3.5" rx="0.6" fill="var(--ink)"/><rect x="2.5" y="6.5" width="5" height="2.5" fill="var(--ink)"/><rect x="3" y="7.2" width="4" height="1.2" fill="var(--paper)"/></svg>
        </div>
        <div class="contact-line">admin@brightmerefinancial.com.au
          <svg viewBox="0 0 10 10" aria-label="Email"><rect x="1" y="2" width="8" height="6" fill="var(--ink)"/><path d="M1.3 2.4 L5 5.3 L8.7 2.4" fill="none" stroke="var(--paper)" stroke-width="0.8"/></svg>
        </div>
        <div class="contact-line">www.brightmerefinancial.com.au
          <svg viewBox="0 0 10 10" aria-label="Website"><circle cx="5" cy="5" r="4.2" fill="var(--ink)"/><path d="M3 3 Q4.5 2.5 4.5 4 Q3.5 5 4.5 6.5 M6.5 5.5 Q7.5 6 6.8 7.6" fill="none" stroke="var(--paper)" stroke-width="0.9"/></svg>
        </div>
      </address>
    </header>

    <svg class="watermark" width="374" height="374" viewBox="0 0 374 374" aria-hidden="true">
      <circle cx="187" cy="187" r="182" fill="none" stroke="var(--faint-mark)" stroke-width="7"/>
    </svg>

    <footer class="footer">
      <div class="footer-licensee">
        Harbourline Financial Planning Limited<br>
        ABN 48 113 620 571<br>
        Australian Financial Services Licence<br>
        Licence Number 318 204<br>
        Principle Address: 410 Elmwood St<br>
        PO Box 1947 Melbourne VIC 3001
      </div>
      <span class="footer-divider first"></span>
      <div class="footer-rep">
        ABN: 62 907 315 480<br>
        Corporate Authorised<br>
        Representative of Harbourline<br>
        Financial Planning Limited
      </div>
      <span class="footer-divider second"></span>
      <div class="footer-trust">
        Wyndale Investments Pty Ltd<br>
        ATF The Ashgrove Investment<br>
        Trust T/AS Brightmere Financial
      </div>
    </footer>
  </main>
</body>
</html>
```